Women's Health Company needs business card

We need a business card for a USA based women's health care company. We use digital technology to enhance therapy prescribed by clinicians for their patients

```html
<!DOCTYPE html>
<html lang="en">
<head>
<meta charset="utf-8">
<title>Novera Health – Business Card</title>
<link rel="stylesheet" href="https://fonts.googleapis.com/css2?family=Roboto:wght@400;500;700&display=swap">
<style>
  :root {
    --stage: #1c1c1c;
    --purple: #8e55a0;
    --teal: #74bfbb;
    --white: #ffffff;
    --paper: #edecec;
    --shadow: rgba(0, 0, 0, 0.85);
  }
  * { box-sizing: border-box; margin: 0; padding: 0; }
  html, body {
    width: 1075px;
    height: 1200px;
    overflow: hidden;
    background: var(--stage);
    font-family: "Roboto", Arial, sans-serif;
  }
  .card {
    position: absolute;
    width: 663px;
    height: 395px;
    overflow: hidden;
    box-shadow: 3px 3px 2px var(--shadow);
  }
  .card--front { left: 206px; top: 187px; background: var(--purple); }
  .card--back { left: 203px; top: 637px; background: var(--paper); }

  .card__waves { position: absolute; inset: 0; width: 100%; height: 100%; }

  .brand-name {
    position: absolute;
    font-weight: 400;
    white-space: nowrap;
    letter-spacing: 0.5px;
  }
  .card--front .brand-name {
    left: 24px;
    top: 172px;
    font-size: 31px;
    color: var(--white);
  }
  .card--back .brand-name {
    left: 0;
    right: 0;
    top: 172px;
    text-align: center;
    font-size: 50px;
    color: var(--teal);
  }

  .contact {
    position: absolute;
    right: 40px;
    top: 110px;
    text-align: right;
    color: var(--white);
  }
  .contact__name { font-size: 23px; font-weight: 700; line-height: 27px; letter-spacing: 0.3px; }
  .contact__role { font-size: 18px; line-height: 22px; }
  .contact__address { margin-top: 22px; font-size: 18px; line-height: 23px; }
  .contact__lines { margin-top: 46px; font-size: 18px; line-height: 24px; list-style: none; }
  .contact__lines li { display: flex; justify-content: flex-end; align-items: center; gap: 7px; }
  .contact__lines svg { width: 17px; height: 17px; flex: none; }
</style>
</head>
<body>

<section class="card card--front" aria-label="Business card front">
  <svg class="card__waves" viewBox="0 0 738 439" preserveAspectRatio="none" aria-hidden="true">
    <path d="M55 439 C 250 375, 330 250, 420 155 C 520 52, 630 -8, 738 4 L738 439 Z" fill="var(--white)"/>
    <path d="M78 439 C 265 385, 345 262, 432 170 C 532 68, 635 10, 738 18 L738 439 Z" fill="var(--teal)"/>
  </svg>

  <div class="brand-name">Novera Health</div>

  <div class="contact">
    <p class="contact__name">DANIEL HARPER</p>
    <p class="contact__role">Managing Director</p>
    <p class="contact__address">421, Address line goes here<br>45452, Country Name</p>
    <ul class="contact__lines">
      <li>044-555 210 347
        <svg viewBox="0 0 24 24" aria-label="Phone"><path fill="var(--white)" d="M6.6 10.8a15.1 15.1 0 0 0 6.6 6.6l2.2-2.2c.3-.3.7-.4 1-.2 1.1.4 2.3.6 3.6.6.6 0 1 .4 1 1V20c0 .6-.4 1-1 1A17 17 0 0 1 3 4c0-.6.4-1 1-1h3.5c.6 0 1 .4 1 1 0 1.3.2 2.5.6 3.6.1.3 0 .7-.2 1z"/></svg>
      </li>
      <li>hello@noverahealth.com
        <svg viewBox="0 0 24 24" aria-label="Email"><rect x="2" y="5" width="20" height="14" fill="var(--white)"/><path d="M2 5l10 8 10-8" fill="none" stroke="var(--teal)" stroke-width="1.5"/></svg>
      </li>
      <li>www.noverahealth.com
        <svg viewBox="0 0 24 24" aria-label="Website"><g fill="none" stroke="var(--white)" stroke-width="1.8"><circle cx="12" cy="12" r="9.5"/><ellipse cx="12" cy="12" rx="4.5" ry="9.5"/><path d="M2.5 12h19M4 7h16M4 17h16"/></g></svg>
      </li>
    </ul>
  </div>
</section>

<section class="card card--back" aria-label="Business card back">
  <div class="brand-name">Novera Health</div>
</section>

</body>
</html>
```